O Balcão KEZ - costumer paper bag

We need a new design for the paper bags of our stores located in Portugal (Funchal and Lisboa).
The design must use logo colors. The final design should comunicate top fashion image, glamour and exclusivity.
We are a gowns and accessories speciality store with 4 fisical locations and online at www.obalcao.pt

Target Market(s)

Mass market, up scale consumers

Industry/Entity Type

Kez

Requirements
Must have
• . keep diamonds in logo of the letters KEZ
• . simple design
• - work only with the colors black, white, silver
• - modern
Nice to have
• elegante and simple design
Should not have
• differente colors other of the mentioned above
• complicated desing

```html
<!DOCTYPE html>
<html lang="pt">
<head>
<meta charset="utf-8">
<title>O Balcão KEZ – Saco de compras</title>
<link rel="stylesheet" href="https://fonts.googleapis.com/css2?family=Questrial&display=swap">
<style>
  :root {
    --page: #a9a8aa;
    --bag: #0b0b0b;
    --white: #f7f7f7;
    --silver: #cfd0d2;
    --silver-dark: #8e9094;
  }
  html, body {
    margin: 0;
    padding: 0;
    width: 1200px;
    height: 1200px;
    overflow: hidden;
    background: var(--page);
  }
  .bag-face {
    position: absolute;
    left: 50px;
    top: 198px;
    width: 1100px;
    height: 804px;
    background: var(--bag);
    overflow: hidden;
  }
  .stripe-field {
    position: absolute;
    right: 0;
    top: 0;
    width: 550px;
    height: 100%;
    background: linear-gradient(90deg, var(--bag) 0%, #5a5a5a 35%, #d8d8d8 100%);
  }
  .brand-name {
    position: absolute;
    left: 280px;
    top: 76px;
    padding: 4px 26px 8px;
    background: var(--bag);
    color: var(--white);
    font-family: "Questrial", sans-serif;
    font-size: 74px;
    line-height: 1;
    letter-spacing: 1px;
  }
  .club-mark {
    position: absolute;
    left: 104px;
    top: 600px;
    margin: 0;
    font-family: "Questrial", sans-serif;
    font-size: 178px;
    line-height: 1;
    letter-spacing: 6px;
    color: var(--silver);
  }
</style>
</head>
<body>
  <main class="bag-face">
    <div class="stripe-field" role="img" aria-label="Padrão de riscas de zebra a preto e branco"></div>
    <div class="brand-name">O Balcão</div>
    <p class="club-mark">KEZ</p>
  </main>
</body>
</html>
```